Post Lockdown Ortho Special

We are running a special for (Ortho) Braces/Clear Aligner (Quorventa), till July 31st 2020. Up to $2,000 off with free Consultation and Xrays.

We need a ad to run in different formats.

Maybe something with: what better time to get braces when you have to wear a mask all the time.

Trying to rebuild our business and get people in for free consultations.

```html
<!DOCTYPE html>
<html lang="en">
<head>
<meta charset="utf-8">
<title>Post Lockdown Ortho Special – Banner Spec</title>
<link href="https://fonts.googleapis.com/css2?family=Arimo:wght@700&family=Archivo+Black&family=Signika:wght@600&family=Poppins:wght@300;800&family=Jost:wght@300;400&display=swap" rel="stylesheet">
<style>
  :root {
    --sheet: #ffffff;
    --guide-grey: #6d6d6d;
    --guide-red: #c8102e;
    --bg-warm: #c9a08a;
    --bg-light: #dcbcaa;
    --bg-dark: #a9765f;
    --ink-plum: #4a1c46;
    --ink-navy: #1e0a4a;
    --accent-red: #b5121b;
    --photo-top: #b99a88;
    --photo-mid: #9c9a9b;
    --photo-low: #d3dadd;
    --white: #ffffff;
  }
  html, body {
    margin: 0;
    padding: 0;
    width: 1200px;
    height: 842px;
    overflow: hidden;
    background: var(--sheet);
  }
  .sheet {
    position: relative;
    width: 1200px;
    height: 842px;
  }
  .guides {
    position: absolute;
    inset: 0;
  }
  .banner {
    position: absolute;
    left: 158px;
    top: 188px;
    width: 861px;
    height: 450px;
    overflow: hidden;
    background:
      radial-gradient(ellipse 60% 80% at 52% 55%, var(--bg-light) 0%, rgba(220,188,170,0) 70%),
      linear-gradient(100deg, var(--bg-dark) 0%, var(--bg-warm) 30%, var(--bg-warm) 70%, var(--bg-dark) 100%);
  }
  .banner-art {
    position: absolute;
    inset: 0;
  }
  .photo-area {
    position: absolute;
    left: 510px;
    top: 46px;
    width: 351px;
    height: 404px;
    background: linear-gradient(180deg, var(--photo-top) 0%, var(--photo-mid) 45%, var(--photo-low) 100%);
  }
  .headline {
    position: absolute;
    margin: 0;
    font-family: "Arimo", Arial, sans-serif;
    font-weight: 700;
    color: var(--white);
    white-space: nowrap;
    text-shadow: 2px 2px 0 var(--ink-plum), 1px 1px 0 var(--ink-plum);
  }
  .headline-main {
    left: 41px;
    top: 50px;
    font-size: 38.7px;
  }
  .headline-sub {
    left: 46px;
    top: 95px;
    font-size: 26.5px;
  }
  .free-label {
    position: absolute;
    left: 119px;
    top: 126px;
    font-family: "Archivo Black", sans-serif;
    font-size: 43px;
    line-height: 44px;
    color: var(--ink-navy);
    transform: scaleX(0.72);
    transform-origin: left center;
  }
  .service {
    position: absolute;
    top: 214px;
    width: 80px;
    text-align: center;
    font-family: "Signika", sans-serif;
    font-weight: 600;
    color: var(--accent-red);
    font-size: 16px;
  }
  .service-consult { left: 74px; font-size: 16px; letter-spacing: -0.3px; }
  .service-xray { left: 163px; }
  .offer-upto {
    position: absolute;
    left: 69px;
    top: 285px;
    font-family: "Poppins", sans-serif;
    font-weight: 300;
    font-size: 35px;
    line-height: 35px;
    letter-spacing: -2.5px;
    color: var(--white);
    text-shadow: 1px 1px 0 #2a1050;
  }
  .offer-off {
    position: absolute;
    left: 67px;
    top: 316px;
    font-family: "Poppins", sans-serif;
    font-weight: 800;
    font-size: 42px;
    line-height: 42px;
    color: var(--white);
  }
  .offer-amount {
    position: absolute;
    left: 165px;
    top: 285px;
    font-family: "Poppins", sans-serif;
    font-weight: 800;
    font-size: 66px;
    line-height: 76px;
    letter-spacing: -2px;
    color: var(--white);
  }
  .offer-deadline {
    position: absolute;
    left: 164px;
    top: 370px;
    font-family: "Jost", sans-serif;
    font-weight: 400;
    font-size: 18px;
    color: var(--ink-navy);
  }
  .legend {
    position: absolute;
    left: 191px;
    top: 722px;
  }
  .legend-item {
    display: flex;
    align-items: center;
    height: 20px;
    font-family: "Jost", sans-serif;
    font-weight: 300;
    font-size: 18px;
  }
  .legend-item::before {
    content: "";
    width: 64px;
    height: 1px;
    margin-right: 14px;
    background: currentColor;
  }
  .legend-social { color: var(--guide-grey); }
  .legend-web { color: var(--guide-red); }
</style>
</head>
<body>
<div class="sheet">

  <svg class="guides" width="1200" height="842" viewBox="0 0 1200 842">
    <defs>
      <marker id="arrow-grey" markerWidth="8" markerHeight="8" refX="7" refY="4" orient="auto-start-reverse">
        <path d="M0,0 L8,4 L0,8 Z" fill="#6d6d6d"/>
      </marker>
      <marker id="arrow-red" markerWidth="8" markerHeight="8" refX="7" refY="4" orient="auto-start-reverse">
        <path d="M0,0 L8,4 L0,8 Z" fill="#c8102e"/>
      </marker>
    </defs>
    <g fill="none" stroke-width="1">
      <line x1="160" y1="125" x2="1017" y2="125" stroke="#c8102e" marker-start="url(#arrow-red)" marker-end="url(#arrow-red)"/>
      <line x1="160" y1="157" x2="1017" y2="157" stroke="#6d6d6d" marker-start="url(#arrow-grey)" marker-end="url(#arrow-grey)"/>
      <line x1="160" y1="669" x2="1017" y2="669" stroke="#6d6d6d" marker-start="url(#arrow-grey)" marker-end="url(#arrow-grey)"/>
      <line x1="160" y1="702" x2="1017" y2="702" stroke="#c8102e" marker-start="url(#arrow-red)" marker-end="url(#arrow-red)"/>
      <line x1="127" y1="190" x2="127" y2="636" stroke="#6d6d6d" marker-start="url(#arrow-grey)" marker-end="url(#arrow-grey)"/>
      <line x1="1050" y1="190" x2="1050" y2="636" stroke="#6d6d6d" marker-start="url(#arrow-grey)" marker-end="url(#arrow-grey)"/>
      <line x1="96" y1="237" x2="96" y2="589" stroke="#c8102e" marker-start="url(#arrow-red)" marker-end="url(#arrow-red)"/>
      <line x1="1080" y1="237" x2="1080" y2="589" stroke="#c8102e" marker-start="url(#arrow-red)" marker-end="url(#arrow-red)"/>
      <g stroke-dasharray="4 3">
        <line x1="158" y1="122" x2="158" y2="188" stroke="#c8102e"/>
        <line x1="1019" y1="122" x2="1019" y2="188" stroke="#c8102e"/>
        <line x1="158" y1="638" x2="158" y2="705" stroke="#c8102e"/>
        <line x1="1019" y1="638" x2="1019" y2="705" stroke="#c8102e"/>
        <line x1="124" y1="188" x2="158" y2="188" stroke="#6d6d6d"/>
        <line x1="1019" y1="188" x2="1053" y2="188" stroke="#6d6d6d"/>
        <line x1="124" y1="638" x2="158" y2="638" stroke="#6d6d6d"/>
        <line x1="1019" y1="638" x2="1053" y2="638" stroke="#6d6d6d"/>
        <line x1="93" y1="234" x2="158" y2="234" stroke="#c8102e"/>
        <line x1="1019" y1="234" x2="1083" y2="234" stroke="#c8102e"/>
        <line x1="93" y1="593" x2="158" y2="593" stroke="#c8102e"/>
        <line x1="1019" y1="593" x2="1083" y2="593" stroke="#c8102e"/>
      </g>
    </g>
  </svg>

  <section class="banner">
    <div class="photo-area" role="img" aria-label="Photo of a smiling woman in a white turtleneck seated in a grey armchair"></div>

    <svg class="banner-art" width="861" height="450" viewBox="0 0 861 450">
      <defs>
        <linearGradient id="hex-fill" x1="0" y1="0" x2="1" y2="0">
          <stop offset="0" stop-color="#b9b9bd"/>
          <stop offset="0.6" stop-color="#eeeeef"/>
          <stop offset="1" stop-color="#ffffff"/>
        </linearGradient>
        <linearGradient id="ribbon-fill" x1="0" y1="0" x2="1" y2="0">
          <stop offset="0" stop-color="#bda6da"/>
          <stop offset="1" stop-color="#6a2db3"/>
        </linearGradient>
        <linearGradient id="curl-fill" x1="0" y1="0" x2="1" y2="0">
          <stop offset="0" stop-color="#d7c6ee"/>
          <stop offset="1" stop-color="#7f4cc2"/>
        </linearGradient>
        <radialGradient id="ball-fill" cx="0.35" cy="0.3" r="0.75">
          <stop offset="0" stop-color="#e6d6fb"/>
          <stop offset="0.45" stop-color="#8a52d6"/>
          <stop offset="1" stop-color="#4b1d8f"/>
        </radialGradient>
        <filter id="ring-glow" x="-20%" y="-20%" width="140%" height="140%">
          <feGaussianBlur stdDeviation="2"/>
        </filter>
      </defs>

      <path d="M108 146 H38 V226 H61" fill="none" stroke="#ffffff" stroke-width="1.5"/>
      <path d="M216 146 H286 V226 H254" fill="none" stroke="#ffffff" stroke-width="1.5"/>

      <g stroke="#ffffff" stroke-width="2" fill="url(#hex-fill)">
        <polygon points="114,182 153,204 153,249 114,272 75,249 75,204"/>
        <polygon points="203,182 242,204 242,249 203,272 164,249 164,204"/>
      </g>

      <path d="M46 283 H405 Q421 283 421 298 V365 H44 L38 357 L44 350 L37 340 L43 332 L36 322 L43 313 L37 303 L44 294 Z" fill="url(#ribbon-fill)"/>
      <line x1="46" y1="365" x2="407" y2="365" stroke="#2a1050" stroke-width="3"/>
      <path d="M404 287 Q421 282 421 298 V384 Q421 393 410 393 H404 Z" fill="url(#curl-fill)" stroke="#2a1050" stroke-width="2.5"/>

      <ellipse cx="673" cy="351" rx="186" ry="86" fill="none" stroke="#f3dcea" stroke-width="5" filter="url(#ring-glow)"/>
      <ellipse cx="673" cy="351" rx="186" ry="86" fill="none" stroke="#ffffff" stroke-width="1.5" opacity="0.8"/>
      <circle cx="490" cy="339" r="15" fill="url(#ball-fill)"/>
    </svg>

    <h1 class="headline headline-main">What better time to get braces</h1>
    <p class="headline headline-sub">when you have to wear a mask all the time?</p>

    <div class="free-label">FREE</div>
    <div class="service service-consult">Consultant</div>
    <div class="service service-xray">Xray</div>

    <div class="offer-upto">UP TO</div>
    <div class="offer-off">OFF</div>
    <div class="offer-amount">$2,000</div>
    <div class="offer-deadline">Till July 31st 2020</div>
  </section>

  <div class="legend">
    <div class="legend-item legend-social">Visible on Friendlane</div>
    <div class="legend-item legend-web">Visible on Website</div>
  </div>

</div>
</body>
</html>
```